Modern CNC Machining Facility in Need of Web Site Improvement

Brixton Fabrication and Tooling, LLC is in need of a web site update. We need to highlight both product sales and our manufacturing services offered. We have recently started offering online product sales and need a better ecommerce platform for our customers. We would like the design winner to be able to freelance the project to a fully functioning webpage.
www.brixtonfabrication.example
What we like about our current web site:
Black and red highlight colors
Gear and caliper logo
RNVR Veteran owned business
What we don't like about our current web site:
Unorganized
Doesn't stand out
Looks like it was made in 1995
Online Product sales are awkward

```html
<!DOCTYPE html>
<html lang="en">
<head>
<meta charset="utf-8">
<title>Brixton Fabrication and Tooling, LLC</title>
<link href="https://fonts.googleapis.com/css2?family=Arimo:wght@400;700&family=Crimson+Text:wght@400;600&family=Cormorant+Garamond:ital,wght@0,600;1,600&display=swap" rel="stylesheet">
<style>
:root{
  --red:#a1030a;
  --red-bright:#c0141b;
  --black:#000;
  --header-bg:#cfd6e0;
  --grey-footer:#b5b5b5;
  --rule:#9a9a9a;
  --heading-grey:#8a8a8a;
  --text:#333;
  --teal:#2a86a8;
  --white:#fff;
}
*{margin:0;padding:0;box-sizing:border-box}
html,body{width:828px;height:1200px;overflow:hidden}
body{position:relative;background:var(--white);font-family:Arimo,Arial,sans-serif;color:var(--text)}
.abs{position:absolute}

.site-header{left:0;top:0;width:828px;height:127px;background:linear-gradient(135deg,#d6dce5 0%,#c8d0dc 50%,#d9dee6 100%)}
.brand{left:70px;top:32px;display:flex;align-items:center;gap:8px;font-family:"Crimson Text",serif;font-weight:600;font-size:17px;color:var(--black);line-height:1.05}
.brand-mark{width:30px;height:30px;border-radius:50%;background:var(--red);flex:none}
.search{left:608px;top:26px;width:150px;height:23px;background:var(--white);border-radius:3px;box-shadow:0 1px 2px rgba(0,0,0,.3);font-family:"Crimson Text",serif;font-size:12px;color:#aaa;padding:4px 0 0 17px}
.search svg{position:absolute;right:18px;top:5px}
.social{left:648px;top:69px;display:flex;gap:10px}
.social span{width:22px;height:22px;border-radius:50%;background:#4d5a6a;display:flex;align-items:center;justify-content:center}

.main-nav{left:0;top:127px;width:828px;height:35px;background:var(--black);display:flex;padding-left:68px}
.main-nav a{color:var(--white);text-decoration:none;font-size:12.5px;line-height:35px;padding:0 10px;margin-right:16px}
.main-nav a.active{background:var(--red-bright)}

.hero{left:0;top:162px;width:828px;height:277px;background:linear-gradient(90deg,#a9b9cc 0%,#d9dfe6 35%,#6c7480 55%,#c6d2df 80%,#8fa8c4 100%)}
.hero-title{left:82px;top:52px;text-align:right;font-family:"Cormorant Garamond",serif;font-weight:600;color:var(--teal);text-shadow:1px 1px 1px rgba(0,0,0,.35)}
.hero-title .big{display:block;font-size:46px;line-height:46px}
.hero-title .and{display:block;font-size:28px;color:#333;line-height:30px}
.hero-title .eng{display:block;font-size:31px;line-height:34px}

.section-title{left:68px;width:692px;display:flex;align-items:center;gap:12px;font-family:"Crimson Text",serif;font-size:20px;color:var(--heading-grey)}
.section-title::before,.section-title::after{content:"";flex:1;height:4px;border-top:1px solid var(--rule);border-bottom:1px solid var(--rule)}
.services-title{top:479px}
.clients-title{top:783px}

.service{top:538px;width:197px;text-align:center}
.service-photo{width:197px;height:132px;border:2px solid #9c9c9c}
.service h3{font-family:"Crimson Text",serif;font-weight:400;font-size:16px;color:#111;margin-top:10px}
.service p{font-size:9px;line-height:14px;color:#444;margin:6px 10px 0}

.clients{left:0;top:852px;width:828px;height:99px;background:var(--red)}
.arrow{top:45px;width:19px;height:19px;background:var(--white);display:flex;align-items:center;justify-content:center}
.client-row{left:104px;top:36px;width:620px;display:flex;justify-content:space-between}
.client{font-family:"Crimson Text",serif;font-weight:600;font-size:22px;color:#2a0c0e}

.site-footer{left:0;top:951px;width:828px;height:208px;background:var(--grey-footer)}
.footer-col{top:22px}
.footer-col h4{font-size:17px;font-weight:400;color:#111;display:inline-block;padding:0 2px 4px;border-bottom:1px solid #222;margin-bottom:12px}
.footer-col p{font-size:9px;line-height:14px;color:#222}
.divider{top:40px;width:1px;height:140px;background:#555}
.news p{line-height:16.5px}
.contact li{list-style:none;display:flex;gap:6px;font-size:9px;line-height:16px;color:#222;margin-bottom:4px}
.contact svg{flex:none;margin-top:2px}

.copyright{left:0;top:1159px;width:828px;height:41px;background:var(--red);text-align:center;font-family:"Crimson Text",serif;font-size:9px;line-height:41px;color:#2a0c0e}
</style>
</head>
<body>

<header class="site-header abs">
  <div class="brand abs"><span class="brand-mark"></span><span>Brixton<br>Fabrication</span></div>
  <div class="search abs">Search...
    <svg width="11" height="11" viewBox="0 0 11 11"><circle cx="4.5" cy="4.5" r="3.4" fill="none" stroke="#999" stroke-width="1.6"/><line x1="7" y1="7" x2="10" y2="10" stroke="#999" stroke-width="1.8"/></svg>
  </div>
  <div class="social abs">
    <span></span><span></span><span></span>
    <span><svg width="12" height="9" viewBox="0 0 12 9"><rect x=".5" y=".5" width="11" height="8" fill="none" stroke="#fff"/><path d="M.5 .5 6 5l5.5-4.5" fill="none" stroke="#fff"/></svg></span>
  </div>
</header>

<nav class="main-nav abs">
  <a class="active" href="#">Home</a>
  <a href="#">Online Product Sales</a>
  <a href="#">Ice Flashing Spears</a>
  <a href="#">Equipment</a>
  <a href="#">Contact-Us</a>
  <a href="#">Brixton Fabrication Blog</a>
</nav>

<section class="hero abs" role="img" aria-label="Photo of young engineering apprentices in a workshop classroom">
  <h1 class="hero-title abs"><span class="big">Manufacturing</span><span class="and">and</span><span class="eng">Engineering</span></h1>
</section>

<h2 class="section-title services-title abs">Services</h2>

<article class="service abs" style="left:70px">
  <div class="service-photo" role="img" aria-label="Engineers in hard hats beside orange industrial robots" style="background:linear-gradient(135deg,#d97a2c,#5f6f86 60%,#2c4f8a)"></div>
  <h3>Lorem Ipsum</h3>
  <p>Lorem Ipsum is simply dummy text of the printing and typesetting industry. Lorem Ipsum has been the industry's standard</p>
</article>
<article class="service abs" style="left:318px">
  <div class="service-photo" role="img" aria-label="Two technicians in lab coats reviewing a tablet" style="background:linear-gradient(135deg,#8a8170,#e6e4df 50%,#6d7c88)"></div>
  <h3>Lorem Ipsum</h3>
  <p>Lorem Ipsum is simply dummy text of the printing and typesetting industry. Lorem</p>
</article>
<article class="service abs" style="left:562px">
  <div class="service-photo" role="img" aria-label="Machinist operating a milling machine" style="background:linear-gradient(135deg,#a9b0ad,#6e7471 50%,#2e2e2e)"></div>
  <h3>Lorem Ipsum</h3>
  <p>Lorem Ipsum is simply dummy text of the printing and typesetting industry. Lorem scrambled it to make a type specimen</p>
</article>

<h2 class="section-title clients-title abs">Our Clients</h2>

<section class="clients abs">
  <div class="arrow abs" style="left:69px"><svg width="6" height="9" viewBox="0 0 6 9"><path d="M5 1 1.5 4.5 5 8" fill="none" stroke="#a1030a" stroke-width="2"/></svg></div>
  <div class="client-row abs">
    <span class="client">Harlow Studio</span><span class="client">Kestrel</span><span class="client">Fenwick</span><span class="client">Harlow Studio</span><span class="client">Kestrel</span>
  </div>
  <div class="arrow abs" style="left:740px"><svg width="6" height="9" viewBox="0 0 6 9"><path d="M1 1 4.5 4.5 1 8" fill="none" stroke="#a1030a" stroke-width="2"/></svg></div>
</section>

<footer class="site-footer abs">
  <div class="footer-col abs" style="left:69px;width:240px">
    <h4>About us</h4>
    <p>Lorem ipsum dolor sit amet, consectetur adipiscing elit. Maecenas sed diam eget risus varius blandit sit amet. Cras mattis consectetur purus sit amet fermentum.</p>
    <p style="margin-top:14px">Maecenas sed diam eget risus varius blandit sit amet non magna. Cras mattis consectetur purus sit amet. Lorem ipsum dolor sit amet. Maecenas sed diam eget risus varius blandit sit amet non magna. Mattis purus sit amet fermentum.</p>
  </div>
  <div class="divider abs" style="left:316px"></div>
  <div class="footer-col news abs" style="left:338px;width:260px">
    <h4>Latest News</h4>
    <p>Another Single Interesting Post</p>
    <p>March 27, 2013</p>
    <p>This is Just a Single Clean Post with Long Interesting Title</p>
    <p>March 08, 2013</p>
    <p>This is a Single Clean Post</p>
    <p>March 06, 2013</p>
  </div>
  <div class="divider abs" style="left:601px"></div>
  <div class="footer-col contact abs" style="left:616px;width:150px">
    <h4 style="margin-left:8px">Contact Info</h4>
    <ul>
      <li><svg width="10" height="13" viewBox="0 0 10 13"><path d="M5 12.5S1 7.5 1 5a4 4 0 0 1 8 0c0 2.5-4 7.5-4 7.5z" fill="#444"/><circle cx="5" cy="5" r="1.5" fill="#b5b5b5"/></svg><span>: Integer posuere erat a ante venenatisdapibus pos uere velit aliquet. Praesent</span></li>
      <li><svg width="11" height="11" viewBox="0 0 11 11"><path d="M2 1l2 2-1 1.5c.8 1.5 1.8 2.5 3.5 3.5L8 7l2 2-1.5 1.5C4.5 10 1 6.5.5 2.5z" fill="#444"/></svg><span>: +44-0123-456-789</span></li>
      <li><svg width="12" height="9" viewBox="0 0 12 9"><rect x=".5" y=".5" width="11" height="8" fill="none" stroke="#444"/><path d="M.5 .5 6 5l5.5-4.5" fill="none" stroke="#444"/></svg><span>: hello@brixtonfabrication.example</span></li>
    </ul>
  </div>
</footer>

<div class="copyright abs">Copyright 2013 All Right Reserved.</div>

</body>
</html>
```